Task Scheduling Web App

I have a basic web app that I need designed. It must be mobile-first but it needs to be responsive for desktop users as well.
1. Before beginning the exercise, the user inputs basic info on their country and age.
2. The user is then presented with two piles of cards (TASK or DAY), with the top card face up. They have 20 seconds before their combination is set, during which they can replace either of the cards at random as many times as they like. At any time they find a combination they’re happy with, they can progress to the next screen. If the clock runs out the combination is set based on whatever cards are showing at the time and they’re moved on to the next screen.
3. The user is presented with a blank graph; x axis is ‘How important is it?’, y axis is ‘How often does it need to be done?’. The two cards they picked in the previous screen are combined to create a COMBO and the user must place a mark somewhere on the graph to represent how important they believe the scheduled task to be vs how often it will need to be done.
4. Once the user has picked a spot on the graph, options appear for them to re-do the exercise by choosing a new combo or to progress and see how their peers are organising their tasks.
5. If they choose to view insights, they must login with Quelvorn so a popup will appear to facilitate this.
6. After logging in with Quelvorn, users can view the top 10 combinations for their demographic listed and mapped on a graph. This information is based on the selection and ranking of combinations by other users.

```html
<!DOCTYPE html>
<html lang="en">
<head>
<meta charset="utf-8">
<title>Your App – Pick a Combo</title>
<link rel="stylesheet" href="https://fonts.googleapis.com/css2?family=Signika:wght@400;600;700&display=swap">
<style>
  :root {
    --page-bg: #ececea;
    --status-bg: #3a3a3a;
    --status-text: #f2f2f2;
    --green: #7fd39a;
    --green-dark: #5fb57c;
    --green-light: #9de3b2;
    --screen-warm-1: #ead8b4;
    --screen-warm-2: #e6c9ad;
    --panel: #f4efe4;
    --ink: #333333;
    --ink-soft: #555555;
    --ink-muted: #6e6e6e;
    --track: #d7d3c9;
    --card: #777777;
    --card-edge: #5a5a5a;
    --card-text: #ffffff;
    --refresh: #ef6f5f;
    --timer-bg: #dedad1;
  }
  * { box-sizing: border-box; margin: 0; padding: 0; }
  html, body { width: 1014px; height: 1200px; overflow: hidden; }
  body {
    background: var(--page-bg);
    font-family: "Signika", sans-serif;
    position: relative;
  }
  .app-screen {
    position: absolute; left: 192px; top: 42px;
    width: 630px; height: 1115px;
    background: radial-gradient(ellipse at 50% 40%, #f1e6cf 0%, var(--screen-warm-1) 55%, var(--screen-warm-2) 100%);
    overflow: hidden;
    box-shadow: 0 4px 18px rgba(0,0,0,.15);
  }
  .status-bar {
    height: 36px; background: var(--status-bg); color: var(--status-text);
    display: flex; align-items: center; justify-content: center;
    font-size: 24px; font-weight: 600; position: relative;
  }
  .status-bar .signal { position: absolute; left: 12px; top: 10px; }
  .status-bar .battery { position: absolute; right: 12px; top: 10px; }
  .top-bar {
    height: 94px; background: linear-gradient(#8bdca5, var(--green));
    border-bottom: 3px solid var(--green-dark);
    display: flex; align-items: center; justify-content: center; position: relative;
  }
  .back-button {
    position: absolute; left: 16px; top: 16px; height: 58px; width: 102px;
    background: var(--green); border: 2px solid var(--green-dark); border-radius: 8px;
    color: #fff; font-size: 26px; font-weight: 600;
    display: flex; align-items: center; justify-content: center; padding-left: 8px;
    clip-path: polygon(14px 0, 100% 0, 100% 100%, 14px 100%, 0 50%);
  }
  .app-name { color: #fff; font-size: 44px; font-weight: 600; }
  .settings-button {
    position: absolute; right: 16px; top: 16px; width: 58px; height: 58px;
    background: #4fa86c; border-radius: 8px;
    display: flex; align-items: center; justify-content: center;
  }
  .panel {
    position: absolute; left: 52px; top: 198px; width: 523px; height: 850px;
    background: var(--panel);
    box-shadow: 0 2px 6px rgba(0,0,0,.08);
  }
  .step-label {
    position: absolute; left: 117px; top: 31px;
    font-size: 18px; font-weight: 600; color: var(--ink-muted); letter-spacing: .5px;
  }
  .progress {
    position: absolute; left: 35px; top: 80px; width: 437px; height: 12px;
    background: var(--track); border-radius: 6px; box-shadow: inset 0 1px 2px rgba(0,0,0,.2);
  }
  .progress-fill { width: 137px; height: 100%; background: var(--green); border-radius: 6px; }
  .progress-knob {
    position: absolute; left: 115px; top: -16px; width: 44px; height: 44px; border-radius: 50%;
    background: radial-gradient(circle at 40% 35%, #ffffff, #bfbfbf 70%, #999);
    box-shadow: 0 2px 4px rgba(0,0,0,.35);
  }
  .screen-title {
    position: absolute; left: 0; right: 0; top: 121px; text-align: center;
    font-size: 45px; font-weight: 700; color: var(--ink);
  }
  .instructions {
    position: absolute; left: 72px; top: 191px; width: 230px;
    font-size: 16px; line-height: 21px; color: var(--ink-soft);
  }
  .timer {
    position: absolute; left: 304px; top: 200px; width: 142px; height: 52px;
    background: var(--timer-bg); border-radius: 26px; box-shadow: inset 0 1px 3px rgba(0,0,0,.2);
    display: flex; align-items: center; justify-content: center;
    font-size: 32px; font-weight: 600; color: var(--ink-muted);
  }
  .deck { position: absolute; left: 20px; width: 460px; }
  .deck-task { top: 283px; height: 195px; }
  .deck-day { top: 510px; height: 198px; }
  .deck-label {
    position: absolute; left: 10px; bottom: 0; width: 40px; height: 100%;
    display: flex; align-items: center; justify-content: center;
  }
  .deck-label span {
    transform: rotate(-90deg); white-space: nowrap;
    font-size: 22px; font-weight: 700; color: var(--ink);
  }
  .card-stack { position: absolute; left: 48px; top: 0; width: 374px; height: 100%; }
  .card {
    position: absolute; inset: 0; border-radius: 14px;
    background: var(--card); border: 2px solid var(--card-edge);
  }
  .card.back-2 { transform: translate(-6px, 6px); background: #666; }
  .card.back-1 { transform: translate(-3px, 3px); background: #6e6e6e; }
  .card.top {
    transform: translate(6px, 0); display: flex; align-items: center; justify-content: center;
    text-align: center; color: var(--card-text); font-weight: 600;
    box-shadow: inset 0 2px 0 rgba(255,255,255,.12);
  }
  .deck-task .card.top { font-size: 32px; line-height: 35px; }
  .deck-day .card.top { font-size: 46px; }
  .refresh-button {
    position: absolute; right: -14px; bottom: -16px; width: 56px; height: 56px; border-radius: 50%;
    background: var(--refresh); border: 3px solid #f7c2b8;
    display: flex; align-items: center; justify-content: center;
    box-shadow: 0 2px 4px rgba(0,0,0,.25);
  }
  .next-button {
    position: absolute; left: 35px; top: 741px; width: 443px; height: 69px;
    background: linear-gradient(var(--green-light), var(--green));
    border: 2px solid var(--green-dark); border-radius: 6px;
    box-shadow: 0 4px 0 #b9c8b8;
    display: flex; align-items: center; justify-content: center;
    color: #fff; font-size: 40px; font-weight: 700; letter-spacing: 1px;
  }
</style>
</head>
<body>
  <main class="app-screen">
    <div class="status-bar">
      <svg class="signal" width="36" height="16" viewBox="0 0 36 16" aria-hidden="true">
        <rect x="0" y="12" width="5" height="4" fill="#f2f2f2"/>
        <rect x="8" y="9" width="5" height="7" fill="#f2f2f2"/>
        <rect x="16" y="6" width="5" height="10" fill="#f2f2f2"/>
        <rect x="24" y="3" width="5" height="13" fill="#f2f2f2"/>
        <rect x="31" y="0" width="5" height="16" fill="#f2f2f2"/>
      </svg>
      <span class="clock">4:20 PM</span>
      <svg class="battery" width="42" height="18" viewBox="0 0 42 18" aria-hidden="true">
        <rect x="1" y="1" width="36" height="16" rx="2" fill="none" stroke="#f2f2f2" stroke-width="2"/>
        <rect x="4" y="4" width="14" height="10" fill="#f2f2f2"/>
        <rect x="38" y="6" width="3" height="6" fill="#f2f2f2"/>
      </svg>
    </div>

    <header class="top-bar">
      <div class="back-button">Back</div>
      <div class="app-name">Your App</div>
      <div class="settings-button">
        <svg width="30" height="30" viewBox="0 0 24 24" aria-label="Settings">
          <path fill="#fff" d="M19.4 13a7.5 7.5 0 0 0 0-2l2.1-1.6-2-3.5-2.5 1a7 7 0 0 0-1.7-1L15 3h-4l-.4 2.9a7 7 0 0 0-1.7 1l-2.5-1-2 3.5L6.6 11a7.5 7.5 0 0 0 0 2l-2.1 1.6 2 3.5 2.5-1a7 7 0 0 0 1.7 1L11 21h4l.4-2.9a7 7 0 0 0 1.7-1l2.5 1 2-3.5zM13 15.5A3.5 3.5 0 1 1 13 8.5a3.5 3.5 0 0 1 0 7z" transform="translate(-1 0)"/>
        </svg>
      </div>
    </header>

    <section class="panel">
      <div class="step-label">STEP 2 OF 6</div>
      <div class="progress">
        <div class="progress-fill"></div>
        <div class="progress-knob"></div>
      </div>

      <h1 class="screen-title">PICK A COMBO</h1>
      <p class="instructions">In 20 seconds, shuffle both decks below to create a combo of your choice.</p>
      <div class="timer">00:20</div>

      <div class="deck deck-task">
        <div class="deck-label"><span>DECK 1: TASK</span></div>
        <div class="card-stack">
          <div class="card back-2"></div>
          <div class="card back-1"></div>
          <div class="card top">Completing<br>office work</div>
          <div class="refresh-button">
            <svg width="30" height="30" viewBox="0 0 24 24" aria-label="Shuffle">
              <path d="M18 12a6 6 0 1 1-2-4.5" fill="none" stroke="#fff" stroke-width="3" stroke-linecap="round"/>
              <path d="M13.5 3.5h5.5v5.5z" fill="#fff"/>
            </svg>
          </div>
        </div>
      </div>

      <div class="deck deck-day">
        <div class="deck-label"><span>DECK 2: DAY</span></div>
        <div class="card-stack">
          <div class="card back-2"></div>
          <div class="card back-1"></div>
          <div class="card top">Monday</div>
          <div class="refresh-button">
            <svg width="30" height="30" viewBox="0 0 24 24" aria-label="Shuffle">
              <path d="M18 12a6 6 0 1 1-2-4.5" fill="none" stroke="#fff" stroke-width="3" stroke-linecap="round"/>
              <path d="M13.5 3.5h5.5v5.5z" fill="#fff"/>
            </svg>
          </div>
        </div>
      </div>

      <div class="next-button">NEXT</div>
    </section>
  </main>
</body>
</html>
```